依頼詳細
2016年に発足した一般吹奏楽団の3回目の演奏会となります。出演者の多くは10代、20代の若い世代が中心となり、音楽を通じて出会った仲間と共に日々活動を行なっています。男女問わず、若い世代からシニア世代まで、たくさんの方々に興味を持ってもらえるようなデザインを希望します。

チラシサイズはA4、チケットサイズは名刺サイズのもので作成お願いします。
チラシ表面には演奏会のイメージとなるものを、チラシ裏面はゲストの紹介及び団の紹介をお願いします。(両面カラー)
チケットはチラシ表面のイメージを使用したものでお願いします。(片面カラー)

【チラシ表面イメージ】
今回の演奏会では「七星の音色」をテーマにしております。
ユニバリアードイヤーにちなんで、七星=五つの大陸にちなんだ選曲をしました。
また、演奏会のメイン曲を交響曲第4番 「ウィンドウズ・オブ・ミナモト」にしました。東京ユニバリアードに開催にあたり、東京周辺の風景を描いた作品を元に作曲された曲を選曲しました。詳細は補足説明をご覧ください。

【チラシ裏面イメージ】
演奏会の一部で、ものまね芸人川端絵美里をゲストに迎え、コラボ企画を予定しております。全体の半分〜3分の2程を使用しゲストの紹介をできるようなものをお願いします。。ゲスト紹介は雑誌の表紙のようなデザインをイメージしております。
(※添付ファイルほか、インターネット上にある画像を使用して構わないとご本人から確認を取っています。)
全体の半分〜3分の1程を使用して当団の紹介。
当団の紹介文や写真を使用して作成をお願いします。

以下、ゲスト紹介の際にご使用ください。
ゲスト:川端 絵美里(ものまね芸人)
現役音楽教師のホンモノを超えたものまね芸
生年月日:11月3日
出身地:福島県
血液型:A型
身長:155cm
趣味:人間観察・映画鑑賞
特技:即興演奏(キーボード)
“ものまね界の帰国子女”鍛え上げられた歌声をご堪能下さい!
[主なネタ]
・即興で作曲(ピアノ弾き語り)
・QRZ36曲中に48人全員のモノマネ
・コラボシリーズ
〜prism×溝口沙耶〜
〜そよかぜびより×溝口沙耶〜
・アーティストから学ぶ音楽授業
…他多数

[主なレパートリー]
柏木美沙(本人公認) 風間千里 溝口沙耶 桐生ゆかり RENVA 水野麻衣 ノラ・ケストリッジ マリエル・ファブロ 古賀弥生 堀田真奈 西浦頼子 北野夏希 Pahama 宮下凛 瀬尾真琴 Tess K. FLARE 澪音 三雲紬 相沢律子 野村さつき VELT 石黒菜穂子 若松ことね ハル子・ブランデル 大槻みほ 森永朱里(きらめきサンフラワーX) 早瀬美智代 宇佐見玲奈 竹みね子 ルシア・ボレンテ ベロニカ・ミナ ポルテリアの世界 CMソングメドレー 羽鳥由紀メドレー 他多数
[主な出演]
ぺんぎんずのみんなでいっしょだよ(ひばりテレビ)クエスト☆芸能図鑑(KRN系)北条健太の水曜日のかがやく人へ(KRN系)ゴゴマルケ!(みなと放送)教えて!ベストテン(かもめテレビ)星組の振り分け☆(かもめテレビ)こだまのMEGAどっきりTV(KRN系)松井茂樹アワー 集まれみんなで!(ひばりテレビ)大笑いうりふたつ声まね東西歌対決スペシャル(ひばりテレビ)マンデーパレード『めざせ妖精王! 川端絵美里のコンビニ減量作戦』(KRN系)ハルミツ・北岡の大捜索!声まねショーコエまね(ひばりテレビ)THEうたごえ☆ファイト『声の職人頂上No.1決定戦』(つばめ放送)Lyra×Lyra(BSひばり)東京スカウトライブ(仮)(TOKYO QV)Pipp!!(KRN系)
記載項目
【チラシ表面】
公演名:第3回演奏会
団体名:みなぎブラスバンド若葉(わかば)
会場:羽村市市民交流会館 そよかぜ 大ホール
日時:2020年5月24日(日)
開場:13:30
開演:14:00
入場料:全席自由 500円
曲目:・ユニバリアード序曲と主題/カール・ベネディクト
・交響曲第4番 「ウィンドウズ・オブ・ミナモト」/マリカ・ボンテ
・委嘱作品/三宅 拓真
・POPS Selection
主催:みなぎブラスバンド若葉
後援:(現在未定)
お問い合わせ:みなぎブラスバンド若葉
wakaba.brass@kazemail.example
その他:会場へのアクセス方法や地図を入れて頂きたいと思います。
また、当団ロゴ、全体写真など使用していただければと思います。(添付ファイル)

【チラシ裏面】
ゲスト紹介については以来詳細をご確認ください。
当団紹介文については600文字程度で現在作成中です。
(チラシデザイン完成後、こちらで追記させていただきます。)
サイズ
A4
ページ数
両面
希望イメージ
シンプル 複雑
単色 カラフル
暗い 明るい
日常 高級
遊び心 厳粛
未来的 伝統的
女性的 男性的
希望する色
設定なし
納品ファイル
• イラストレーター形式 (.ai)
補足説明
交響曲第4番 「ウィンドウズ・オブ・ミナモト」
この曲は梅村雪舟や鳥居春泉の有名な版画6点をモチーフにした、歴史的な日本の木版画にインスピレーションをうけて作曲された6楽章からなる交響曲です。
1. 富士山 (雪舟-名峰四十八図)
2. 日本橋 (鳥居春泉-西国街道六十宿)
3. 相模灘荒波図 (雪舟-名峰四十八図)
4. 銀鶴山清月院 (鳥居春泉-清月院の風神門)
5. 原宿 月之霜 (鳥居春泉-西国街道六十宿)
6. 箱根 (鳥居春泉-西国街道六十宿)

```html
<!DOCTYPE html>
<html lang="ja">
<head>
<meta charset="utf-8">
<title>みなぎブラスバンド若葉 第3回 演奏会</title>
<link rel="stylesheet" href="https://fonts.googleapis.com/css2?family=Noto+Sans+JP:wght@400;500;700;900&display=swap">
<style>
  :root {
    --green: #239a48;
    --green-dark: #16763a;
    --red: #e1303a;
    --ink: #2a2a2a;
    --paper: #ffffff;
    --photo-top: #6a5a4c;
    --photo-bottom: #2d2622;
    --map-bg: #e9efe6;
    --deco-a: rgba(240,138,36,0.35);
    --deco-b: rgba(47,143,214,0.25);
  }
  * { margin: 0; padding: 0; box-sizing: border-box; }
  html, body { width: 849px; height: 1200px; overflow: hidden; background: var(--paper); }
  body { font-family: "Noto Sans JP", sans-serif; color: var(--ink); }
  .flyer { position: relative; width: 849px; height: 1200px; overflow: hidden; background: var(--paper); }

  .corner-deco { position: absolute; left: 0; top: 0; width: 260px; height: 160px;
    background: linear-gradient(150deg, var(--deco-a), var(--deco-b) 55%, rgba(255,255,255,0) 85%); }

  .ensemble-name { position: absolute; left: 240px; top: 22px; width: 460px; text-align: center;
    font-size: 23px; font-weight: 700; color: var(--green); letter-spacing: 1px; }

  .client-mark { position: absolute; right: 26px; top: 22px; width: 92px; text-align: center; }
  .client-mark .dot { width: 70px; height: 70px; border-radius: 50%; background: var(--green); margin: 0 auto 4px; }
  .client-mark .label { font-size: 13px; font-weight: 700; color: var(--green); }

  .concert-title { position: absolute; left: 250px; top: 58px; font-size: 66px; font-weight: 900;
    color: var(--green); letter-spacing: 2px; line-height: 1; }
  .concert-title .num { font-size: 86px; }

  .venue { position: absolute; left: 30px; top: 170px; font-size: 19px; font-weight: 700; color: var(--green); line-height: 1.35; }
  .venue .hall { display: block; padding-left: 58px; }
  .admission { position: absolute; left: 30px; top: 228px; font-size: 19px; font-weight: 700; color: var(--green); }

  .date { position: absolute; right: 34px; top: 168px; text-align: right; color: var(--green); font-weight: 900; }
  .date .day { font-size: 36px; line-height: 1.1; }
  .date .times { font-size: 21px; font-weight: 700; margin-top: 4px; }

  .group-photo { position: absolute; left: 40px; top: 268px; width: 770px; height: 452px;
    background: linear-gradient(180deg, var(--photo-top), var(--photo-bottom)); }

  .clef-deco { position: absolute; left: 620px; top: 820px; width: 200px; height: 310px;
    background: radial-gradient(ellipse at center, rgba(35,154,72,0.16), rgba(35,154,72,0) 70%); }

  .program { position: absolute; left: 30px; top: 744px; width: 790px; font-size: 18px; font-weight: 700; color: var(--green-dark); }
  .program .label { position: absolute; left: 0; top: 0; }
  .program ol { list-style: none; margin-left: 58px; }
  .program li { line-height: 30px; }
  .program .note { color: var(--red); font-size: 14.5px; font-weight: 500; line-height: 1.55; margin: 2px 0 4px 18px; width: 600px; }
  .program .movements { color: var(--red); font-size: 14.5px; font-weight: 500; line-height: 21px; margin: 0 0 4px 18px; }

  .access { position: absolute; left: 30px; top: 1056px; color: var(--green-dark); }
  .access h2 { font-size: 17px; font-weight: 700; }
  .access .address { font-size: 15px; padding-left: 20px; }
  .access-map { position: absolute; left: 48px; top: 1102px; width: 170px; height: 52px; background: var(--map-bg); }

  .credits { position: absolute; left: 30px; right: 30px; top: 1162px; font-size: 14px; font-weight: 700; color: var(--green-dark); line-height: 18px; }
  .credits .row { display: flex; justify-content: space-between; }
</style>
</head>
<body>
<main class="flyer">
  <div class="corner-deco" role="img" aria-label="色とりどりの装飾帯"></div>

  <p class="ensemble-name">みなぎブラスバンド若葉</p>

  <div class="client-mark">
    <div class="dot"></div>
    <div class="label">若葉</div>
  </div>

  <h1 class="concert-title">第<span class="num">3</span>回 演奏会</h1>

  <p class="venue">会場：羽村市市民交流会館<span class="hall">そよかぜ 大ホール</span></p>
  <p class="admission">入場料：全席自由 500円</p>

  <div class="date">
    <p class="day">2020年5月24日(日)</p>
    <p class="times">開場：13:30　開演：14:00</p>
  </div>

  <div class="group-photo" role="img" aria-label="楽器を持って並ぶ団員の全体写真"></div>

  <div class="clef-deco" role="img" aria-label="ト音記号の装飾"></div>

  <section class="program">
    <span class="label">曲目：</span>
    <ol>
      <li>1. ユニバリアード序曲と主題／カール・ベネディクト</li>
      <li>2. 交響曲第4番「ウィンドウズ・オブ・ミナモト」／マリカ・ボンテ</li>
      <li class="note">梅村雪鳴や鳥居春泉の有名な版画6点をモチーフにした、歴史的な日本の木版画にインスピレーションをうけて作曲された6楽章からなる交響曲です。</li>
      <li class="movements">
        1. 富士山（雪鳴-名峰四十八図）<br>
        2. 日本橋（鳥居春泉-西国街道六十宿）<br>
        3. 相模灘荒波図（雪鳴-名峰四十八図）<br>
        4. 銀鶴山清月院（鳥居春泉-清月院の風神門）<br>
        5. 原宿 月之霜（鳥居春泉-西国街道六十宿）<br>
        6. 箱根（鳥居春泉-西国街道六十宿）
      </li>
      <li>3. 委嘱作品／三宅 拓真</li>
      <li>4. POPS Selection</li>
    </ol>
  </section>

  <section class="access">
    <h2>会場までのアクセス：</h2>
    <p class="address">羽村市若草ヶ丘二丁目8番地3</p>
  </section>
  <div class="access-map" role="img" aria-label="会場周辺の地図"></div>

  <footer class="credits">
    <div class="row"><span>主催：みなぎブラスバンド若葉</span><span>後援：(現在未定)</span></div>
    <div class="row"><span>お問い合わせ：みなぎブラスバンド若葉</span><span>wakaba.brass@kazemail.example</span></div>
  </footer>
</main>
</body>
</html>
```